International Dental Education Website

This project is for a small teaching center on endodontic and micro dentistry in Norway. We need a Wordpress website design to display and highlight dental educational courses. Please use our new logo - see attached file. We like lighter, pastel oriented colors. The following sites are nicely laid out and you can use these as a guideline of sorts but I do want a unique site.
http://vorplex.example/en, http://www.toothmarlow.example/Education.aspx?currentSection=courses&cid=14,
http://www.pulpvesker.example/.
Please create a space for a possible video on the home page. Please include a small contact form on the home page(name, email, phone, text box). Would like a horizonatal naviagtion bar. Would like an image to go across the whole top part of the site and this may rotate. Please use a stock image that shows a classroom type setting. Put phone number at the top of the screen. Put address and sitemap in a footer.

Reason: Upcoming vacation with limited internet access. Please continue to submit any designs. Thanks you.

Reason: The client is from a foreign country and is on an extended vacation.

Target Market(s)

General dentists (GPs) and specialists in Endodontics

Industry/Entity Type

Dental

Requirements
Must have
• Sitemap: HOME, COURSES, LECTURER, CONTACT US,
NORWEGIAN/ENGLISH. Phone number is: +47 93516270. Business name and address: Kali Rom AS, Endodontic Teaching Center,
Fjeldstads vei 17C, 0371 Oslo, Norway.

```html
<!DOCTYPE html>
<html lang="en">
<head>
<meta charset="utf-8">
<title>Kali Rom – Endodontic Teaching Center</title>
<link rel="stylesheet" href="https://fonts.googleapis.com/css2?family=Pathway+Gothic+One&family=Arimo:wght@400;700&display=swap">
<style>
:root{
  --teal:#86d0d6;
  --teal-mid:#5bbcc4;
  --teal-dark:#3c9ea4;
  --teal-deep:#2f8f95;
  --ice:#e2fbfd;
  --ice-border:#9fd9dd;
  --field:#dcfafc;
  --field-border:#8fbcc4;
  --grey:#8f999c;
  --grey-dark:#5d6668;
  --ink:#111;
  --white:#fff;
}
*{box-sizing:border-box;margin:0;padding:0}
html,body{width:1200px;height:951px;overflow:hidden;background:var(--white)}
body{position:relative;font-family:"Arimo",Arial,sans-serif;color:var(--ink)}

.brand{position:absolute;left:105px;top:26px;display:flex;align-items:center;gap:8px;
  font-family:"Pathway Gothic One",sans-serif;font-size:40px;color:var(--teal-mid);line-height:1}
.brand-dot{width:14px;height:14px;border-radius:50%;background:var(--teal)}

.call{position:absolute;right:98px;top:8px;font-family:"Pathway Gothic One",sans-serif;
  font-size:21px;color:var(--grey);letter-spacing:.2px}

.nav{position:absolute;left:380px;top:90px;width:441px;height:29px}
.nav svg{position:absolute;inset:0}
.nav ul{position:absolute;inset:0;list-style:none;font-family:"Pathway Gothic One",sans-serif;font-size:19px;color:var(--white)}
.nav li{position:absolute;top:5px}

.lang{position:absolute;left:983px;top:95px;font-family:"Pathway Gothic One",sans-serif;font-size:16px;color:var(--teal)}
.lang .active{color:var(--grey)}
.lang .sep{color:var(--grey);margin:0 4px}

.hero{position:absolute;left:99px;top:118px;width:1003px;height:380px;border:1px solid var(--teal)}
.hero-photo{position:absolute;left:0;top:0;width:1001px;height:340px;
  background:linear-gradient(180deg,#6d6b5f 0%,#a58f72 35%,#c9b295 65%,#9a8a78 100%)}
.hero-band{position:absolute;left:0;top:340px;width:1001px;height:38px;background:var(--teal)}
.hero-band svg{position:absolute;left:0;top:0}
.hero-tag{position:absolute;left:48px;top:7px;font-family:"Pathway Gothic One",sans-serif;font-size:21px;color:var(--white)}
.hero-title{position:absolute;right:16px;top:2px;font-family:"Pathway Gothic One",sans-serif;font-size:32px;color:var(--teal-dark)}
.hero-shadow{position:absolute;left:120px;top:498px;width:960px;height:14px;
  background:radial-gradient(ellipse at 50% 0,rgba(0,0,0,.28),rgba(0,0,0,0) 70%)}

.headline{position:absolute;left:96px;top:508px;font-family:"Pathway Gothic One",sans-serif;font-weight:400;
  font-size:60px;line-height:1;white-space:nowrap;color:var(--teal-mid);
  transform:scaleX(.905);transform-origin:0 0;
  background:linear-gradient(180deg,#7fd0d6 0%,#3b9fa6 100%);-webkit-background-clip:text;background-clip:text;-webkit-text-fill-color:transparent}

.panel{position:absolute;left:98px;top:571px;width:1003px;height:277px;background:var(--ice);border:1px solid var(--ice-border)}
.video{position:absolute;left:7px;top:7px;width:435px;height:262px;
  background:linear-gradient(135deg,#2d3c8c 0%,#6e3a2f 45%,#b69070 75%,#3a4f6d 100%)}
.video-bar{position:absolute;left:0;bottom:0;width:100%;height:26px;background:#1b1b1b}
.video-bar i{position:absolute;left:0;top:0;height:3px;width:100%;background:#c8222a}
.video-play{position:absolute;left:188px;top:100px;width:58px;height:40px;border-radius:9px;background:rgba(20,20,20,.85)}
.video-play svg{position:absolute;left:21px;top:11px}

.intro{position:absolute;left:470px;top:6px;width:231px}
.intro h2{font-family:"Pathway Gothic One",sans-serif;font-weight:400;font-size:22px;line-height:21px;color:var(--teal-dark)}
.intro .rule{height:2px;margin:2px 0 6px;background:linear-gradient(90deg,var(--teal-mid),rgba(91,188,196,0))}
.intro p{font-size:12px;line-height:14.5px;letter-spacing:-.35px;text-align:justify;margin-bottom:13px}

.contact{position:absolute;left:825px;top:551px;width:250px;height:314px;background:var(--white);
  border:2px solid #d3d6d7;border-radius:8px}
.contact h3{text-align:center;font-family:"Pathway Gothic One",sans-serif;font-weight:400;font-size:18px;line-height:22px;color:var(--teal-mid);margin-top:10px}
.contact h4{text-align:center;font-family:"Pathway Gothic One",sans-serif;font-weight:400;font-size:17px;line-height:22px;color:var(--grey)}
.contact .rule{height:1px;margin:3px 40px 0;background:linear-gradient(90deg,rgba(143,188,196,0),var(--teal),rgba(143,188,196,0))}
.field{position:absolute;left:16px;width:211px;background:var(--field);border:1px solid var(--field-border);
  border-radius:5px;font-size:11px;letter-spacing:.8px;color:var(--grey);padding:5px 6px}
.submit{position:absolute;left:81px;top:257px;width:80px;height:24px;border-radius:3px;
  background:linear-gradient(180deg,#56b9bf,#2a8d94);color:var(--white);font-weight:700;font-size:11px;
  text-align:center;line-height:24px;box-shadow:0 7px 6px -5px rgba(0,0,0,.45)}

.footer{position:absolute;left:97px;top:884px;width:1005px;height:67px;border-radius:10px 10px 0 0;
  background:linear-gradient(90deg,var(--teal) 0%,#93d7dc 70%,#c4eef0 83%,var(--teal) 84%,var(--teal) 100%);overflow:hidden}
.footer svg.chev{position:absolute;left:0;top:0}
.footer-brand{position:absolute;left:20px;top:14px;font-family:"Pathway Gothic One",sans-serif;font-size:34px;color:var(--teal-dark);line-height:1}
.footer-address{position:absolute;left:189px;top:27px;font-size:11px;font-weight:700;color:var(--white)}
.footer-divider{position:absolute;left:838px;top:0;width:1px;height:67px;background:rgba(255,255,255,.6)}
.footer-link{position:absolute;top:11px;width:60px;text-align:center;font-size:11px;font-weight:700;color:var(--white)}
.footer-link .dot{display:block;width:30px;height:30px;margin:0 auto 3px;border-radius:50%;
  background:linear-gradient(180deg,#7fd3d9,#2f959b);border:1px solid rgba(255,255,255,.5)}
</style>
</head>
<body>

<header>
  <div class="brand"><span class="brand-dot"></span>Kali Rom</div>
  <div class="call">CALL US : +47 93516270</div>

  <nav class="nav">
    <svg width="441" height="29" viewBox="0 0 441 29">
      <path d="M0 29 L6 8 Q9 0 18 0 L423 0 Q432 0 435 8 L441 29 Z" fill="#86d0d6"/>
      <path d="M60 0 L66 6 L72 0 Z" fill="#fff"/>
    </svg>
    <ul>
      <li style="left:52px">HOME</li>
      <li style="left:128px">COURSES</li>
      <li style="left:222px">LECTURER</li>
      <li style="left:312px">CONTACT US</li>
    </ul>
  </nav>

  <div class="lang">NORWEGIAN<span class="sep">/</span><span class="active">ENGLISH</span></div>
</header>

<section class="hero">
  <div class="hero-photo" role="img" aria-label="Photo of a lecturer teaching a full tiered classroom of students"></div>
  <div class="hero-band">
    <svg width="300" height="38" viewBox="0 0 300 38">
      <path d="M0 0 L296 0 L258 38 L0 38 Z" fill="#6c7476" opacity=".85"/>
      <circle cx="22" cy="19" r="15" fill="#111"/>
      <path d="M15 12 Q22 9 29 12 Q31 18 27 27 L25 22 L22 21 L19 22 L17 27 Q13 18 15 12 Z" fill="#fff"/>
    </svg>
    <div class="hero-tag">DENTAL EDUCATIONAL COURSES</div>
    <div class="hero-title">ENDODONTIC TEACHING CENTER</div>
  </div>
</section>
<div class="hero-shadow"></div>

<h1 class="headline">YOUR SOURCE FOR ENDODONTIC EDUCATION</h1>

<main class="panel">
  <div class="video" role="img" aria-label="Embedded course video of a presenter in a studio">
    <div class="video-play"><svg width="18" height="18" viewBox="0 0 18 18"><path d="M2 1 L17 9 L2 17 Z" fill="#fff"/></svg></div>
    <div class="video-bar"><i></i></div>
  </div>
  <article class="intro">
    <h2>ENDODONTIC TEACHING CENTER<br>DENTAL EDUCATION COURSES</h2>
    <div class="rule"></div>
    <p>ORVEX is an ultra modern centre of dental excellence which offers the very latest in innovative dental education courses. ORVEX is located in an elegant townhouse with a modern interior which exudes a calm atmosphere. It is the ideal surrounding to share knowledge and explore and develop new practical competencies.</p>
    <p>We at ORVEX are convinced you will feel at home while we guide you to efficiently build effective new competencies and ideas which will contribute to perfecting your own practice execution.</p>
  </article>
</main>

<aside class="contact">
  <h3>WE LOOK FORWARD TO WELCOMING YOU!</h3>
  <h4>MESSAGE US YOUR QUESTIONS</h4>
  <div class="rule"></div>
  <div class="field" style="top:68px;height:24px">Name</div>
  <div class="field" style="top:99px;height:23px">Email</div>
  <div class="field" style="top:129px;height:23px">Phone /Mobile</div>
  <div class="field" style="top:159px;height:88px">Message</div>
  <div class="submit">SUBMIT</div>
</aside>

<footer class="footer">
  <svg class="chev" width="200" height="67" viewBox="0 0 200 67">
    <path d="M0 0 L150 0 L182 33 L150 67 L0 67 Z" fill="#9fdde1"/>
    <path d="M124 0 L150 0 L182 33 L150 67 L124 67 L156 33 Z" fill="#b8e8eb"/>
  </svg>
  <div class="footer-brand">Kali Rom</div>
  <div class="footer-address">Kali Rom AS, Endodontic Teaching Center, Fjeldstads vei 17C, 0371 Oslo, Norway.</div>
  <div class="footer-divider"></div>
  <div class="footer-link" style="left:853px"><span class="dot"></span>Join us</div>
  <div class="footer-link" style="left:922px"><span class="dot"></span>Sitemap</div>
</footer>

</body>
</html>
```